Premium Juice and Wine Bottle Label

We require a premium label design for a Burgundy style wine bottle - the design should reflect pure and organic theme, with a reference to New Zealand blueberries. The winning design will look high-end, simple but sophisticated. Our logo is attached, refer :

https://www.orvalecellars.co.nz and https://www.pirovane.co.nz/wines/details/coming-soon-showcase/2018

for inspiration.

Target Market(s)

High-end retail grocery stores, wine shops, bars.

Requirements
Must have
• Label should leave enough space for barcode and nutrients/ingredients etc. Reference to New Zealand, natural-beverage, be very high-end in design. Refer links in project description for inspiration. Refer to attached logo, which must be used - feel free to change colour in order to obtain the best high-class design.
Nice to have
• N/A.
Should not have
• Cartoons or pictures of berries.

```html
<!DOCTYPE html>
<html lang="en">
<head>
<meta charset="utf-8">
<title>Marlow Ridge – Burgundy Wine Labels</title>
<link rel="stylesheet" href="https://fonts.googleapis.com/css2?family=Playfair+Display:wght@700;900&family=Merriweather:ital,wght@0,400;1,400&display=swap">
<style>
  :root {
    --bg: #1c1c1c;
    --label: #f1f1f1;
    --label-edge: #e2e2e2;
    --gold: #a88a4f;
    --gold-light: #cdb27a;
    --ink: #5a5a5a;
    --ink-soft: #6e6e6e;
    --faint: #e3e3e3;
    --blank: #fafafa;
  }
  * { margin: 0; padding: 0; box-sizing: border-box; }
  html, body { width: 1200px; height: 926px; overflow: hidden; background: var(--bg); }
  .stage { position: relative; width: 1200px; height: 926px; }

  /* Front label */
  .front-label {
    position: absolute; left: 90px; top: 290px; width: 420px; height: 450px;
    background: var(--label); border-radius: 12px;
  }
  .brand-tab {
    position: absolute; left: 50%; top: -44px; transform: translateX(-50%);
    width: 170px; height: 96px; background: var(--label); border-radius: 12px;
    display: flex; align-items: center; justify-content: center;
  }
  .brand-name {
    font-family: "Playfair Display", serif; font-weight: 700; font-size: 24px;
    color: var(--gold); text-align: center; line-height: 1.05;
  }
  .product-title {
    position: absolute; top: 84px; width: 100%; text-align: center;
    font-family: "Playfair Display", serif; font-weight: 900; font-size: 56px;
    line-height: 1.05; letter-spacing: 1px; color: var(--gold);
  }
  .berry-art {
    position: absolute; left: 26px; top: 240px; width: 130px; height: 150px;
    background: var(--faint); border-radius: 50%; opacity: .7;
  }
  .map-art {
    position: absolute; right: 30px; top: 205px; width: 120px; height: 200px;
    background: linear-gradient(160deg, var(--faint), #e9e9e9); border-radius: 40% 20% 50% 30%; opacity: .8;
  }
  .origin {
    position: absolute; top: 250px; width: 100%; text-align: center;
    font-family: "Merriweather", serif; font-size: 26px; line-height: 1.35; color: var(--ink);
  }
  .spec {
    position: absolute; bottom: 18px;
    font-family: "Merriweather", serif; font-style: italic; font-size: 17px; color: var(--ink-soft);
  }
  .spec--abv { left: 16px; }
  .spec--volume { right: 22px; }

  /* Back label */
  .back-label {
    position: absolute; left: 700px; top: 300px; width: 400px; height: 420px;
    background: var(--label); border-radius: 2px; padding: 22px 22px 0 22px;
  }
  .back-map {
    position: absolute; right: 30px; top: 80px; width: 150px; height: 300px;
    background: linear-gradient(160deg, var(--faint), #ebebeb); border-radius: 40% 20% 50% 30%; opacity: .7;
  }
  .back-brand {
    position: relative; font-family: "Playfair Display", serif; font-weight: 700;
    font-size: 16px; color: var(--gold); line-height: 1.05; margin: 6px 0 18px;
  }
  .back-copy {
    position: relative; font-family: "Merriweather", serif; font-size: 11px;
    line-height: 1.2; color: var(--ink); margin-bottom: 14px;
  }
  .back-origin {
    position: relative; font-family: "Merriweather", serif; font-style: italic;
    font-size: 16px; color: var(--ink); margin: 14px 0 18px;
  }
  .back-spec {
    position: relative; font-family: "Merriweather", serif; font-style: italic;
    font-size: 15px; color: var(--ink); line-height: 1.75;
  }
  .barcode-space {
    position: absolute; right: 26px; bottom: 34px; width: 180px; height: 72px;
    background: var(--blank);
  }
</style>
</head>
<body>
<main class="stage">
  <section class="front-label">
    <div class="brand-tab"><span class="brand-name">Marlow<br>Ridge</span></div>
    <h1 class="product-title">BURGUNDY<br>WINE</h1>
    <div class="berry-art" role="img" aria-label="Faint embossed outline of berries and leaves"></div>
    <div class="map-art" role="img" aria-label="Faint map of New Zealand"></div>
    <p class="origin">New Zealand<br>2019</p>
    <span class="spec spec--abv">13.5% vol.</span>
    <span class="spec spec--volume">750 ml</span>
  </section>

  <section class="back-label">
    <div class="back-map" role="img" aria-label="Faint map of New Zealand"></div>
    <div class="back-brand">Marlow<br>Ridge</div>
    <p class="back-copy">Hand picked from cool southern slopes, this wine is fermented slowly and aged gently in French oak to keep its bright fruit, soft tannins and long, clean finish.</p>
    <p class="back-copy">Serve lightly chilled with roast lamb, mushrooms or aged cheese. Enjoy now or cellar for up to eight years.</p>
    <p class="back-origin">Made in New Zealand</p>
    <p class="back-spec">13.5% Vol<br>750ml</p>
    <div class="barcode-space"></div>
  </section>
</main>
</body>
</html>
```